Mortgage Broker Site

Need a custom design for a mortgage broker site - please refer to the attached Word .doc that gives more detail.

Number of Pages Required

5+ page

Colors

Designer to choose colors to be used in the design.

```html
<!DOCTYPE html>
<html lang="en">
<head>
<meta charset="utf-8">
<title>Hearthline – Mortgage Refinance Loans</title>
<link href="https://fonts.googleapis.com/css2?family=Oswald:wght@500;600&family=Poppins:wght@400;500;600&family=Hind:wght@400;500&display=swap" rel="stylesheet">
<style>
:root{
  --red:#c4001f;
  --red-dark:#960b21;
  --ink:#333333;
  --text:#4a4a4a;
  --light:#f1f1f1;
  --white:#ffffff;
}
*{box-sizing:border-box;margin:0;padding:0}
html,body{width:911px;height:1200px;overflow:hidden;background:var(--white)}
body{position:relative;font-family:"Poppins",sans-serif;color:var(--text)}
.abs{position:absolute}

/* header */
.site-header{left:0;top:0;width:911px;height:61px;background:var(--white)}
.brand{display:flex;align-items:center;gap:6px;font-family:"Poppins",sans-serif;font-weight:500;font-size:21px;color:var(--ink)}
.brand-mark{width:9px;height:9px;background:var(--red)}
.site-header .brand{left:118px;top:16px}
.main-nav{left:352px;top:30px;display:flex;font-family:"Hind",sans-serif;font-weight:500;font-size:10px;letter-spacing:.4px;color:var(--ink)}
.main-nav span{position:absolute;white-space:nowrap}
.btn-apply{left:706px;top:23px;width:95px;height:26px;border-radius:13px;background:var(--red-dark);color:var(--white);font-family:"Hind",sans-serif;font-weight:500;font-size:10px;letter-spacing:.4px;display:flex;align-items:center;justify-content:center}

/* hero */
.hero{left:0;top:61px;width:911px;height:366px;background:linear-gradient(100deg,#6e6a66 0%,#4d4b4c 40%,#3b4250 70%,#5c5a5a 100%)}
.hero-title{left:0;top:92px;width:911px;text-align:center;font-family:"Oswald",sans-serif;font-weight:600;font-size:39px;color:var(--white);letter-spacing:.3px}
.hero-lead{left:0;top:143px;width:911px;text-align:center;font-family:"Hind",sans-serif;font-size:12.5px;line-height:18px;color:var(--white)}
.btn-outline{left:385px;top:198px;width:134px;height:37px;border:2px solid var(--white);border-radius:19px;color:var(--white);font-family:"Hind",sans-serif;font-weight:500;font-size:12.5px;display:flex;align-items:center;justify-content:center;letter-spacing:.4px}
.slider-lines{left:803px;top:126px}

/* feature cards */
.red-rule{left:0;top:427px;width:911px;height:4px;background:var(--red)}
.light-section{left:0;top:431px;width:911px;height:369px;background:var(--light)}
.feature-pill{left:118px;top:368px;width:675px;height:120px;border-radius:60px;overflow:hidden;display:flex}
.feature{position:relative;width:50%;height:100%;display:flex;align-items:center;color:var(--white)}
.feature--calc{background:var(--red)}
.feature--home{background:var(--red-dark)}
.feature-icon{width:58px;height:56px;border-radius:8px;background:linear-gradient(135deg,#7fbf5a,#f2c64a 60%,#e04a4a);margin-right:16px}
.feature--calc .feature-icon{margin-left:44px}
.feature--home .feature-icon{margin-left:28px}
.feature h3{font-family:"Oswald",sans-serif;font-weight:500;font-size:15px;letter-spacing:.3px;margin-bottom:6px}
.feature p{font-family:"Hind",sans-serif;font-size:10.5px;line-height:18px}

/* loan limits */
.kicker{left:0;top:531px;width:911px;text-align:center;font-family:"Hind",sans-serif;font-weight:500;font-size:13px;color:var(--red-dark)}
.limits-title{left:0;top:547px;width:911px;text-align:center;font-family:"Oswald",sans-serif;font-weight:600;font-size:32px;color:var(--ink)}
.limits-text{left:0;top:604px;width:911px;text-align:center;font-family:"Hind",sans-serif;font-size:10.5px;line-height:21px;color:var(--text)}
.search{left:312px;top:669px;width:297px;height:40px;border:1px solid var(--red-dark);border-radius:20px;background:var(--white)}
.search span{position:absolute;left:21px;top:12px;font-family:"Hind",sans-serif;font-size:11px;color:#888}
.search-btn{position:absolute;right:-1px;top:-1px;width:42px;height:40px;border-radius:20px;background:var(--red-dark);display:flex;align-items:center;justify-content:center}
.neighborhood{left:0;top:732px;width:911px;height:62px;background:linear-gradient(180deg,rgba(200,200,200,0) 0%,rgba(190,190,190,.45) 100%)}

/* call to action */
.cta{left:0;top:800px;width:911px;height:223px;background:linear-gradient(120deg,#3d4a3a 0%,#4b4540 45%,#3a4638 100%)}
.cta-kicker{left:0;top:858px;width:911px;text-align:center;font-family:"Hind",sans-serif;font-weight:500;font-size:15.5px;color:var(--white)}
.cta-title{left:0;top:874px;width:911px;text-align:center;font-family:"Oswald",sans-serif;font-weight:600;font-size:28px;color:var(--white)}
.btn-phone{left:361px;top:927px;width:189px;height:44px;border-radius:22px;background:var(--red-dark);color:var(--white);display:flex;align-items:center;justify-content:center;gap:14px;font-family:"Poppins",sans-serif;font-weight:600;font-size:14px}

/* footer */
.site-footer .brand{left:125px;top:1058px;font-size:22px}
.socials{left:125px;top:1114px;display:flex;gap:5px}
.socials i{display:block;width:18px;height:16px}
.copyright{left:126px;top:1151px;font-size:7.5px;line-height:15px;color:var(--ink)}
.copyright b{font-weight:600}
.foot-col h4{font-family:"Poppins",sans-serif;font-weight:600;font-size:10.5px;color:var(--ink);margin-bottom:12px}
.foot-col li{list-style:none;font-size:9px;line-height:18.2px;color:var(--ink)}
</style>
</head>
<body>

<header class="site-header abs">
  <div class="brand abs"><span class="brand-mark"></span>Hearthline</div>
  <nav class="main-nav abs">
    <span style="left:0">RATES</span>
    <span style="left:55px">PURCHASE</span>
    <span style="left:132px">REFINANCE</span>
    <span style="left:199px;top:-1px">SCHEDULE A CALL</span>
    <span style="left:307px;top:-1px">GUIDE</span>
  </nav>
  <div class="btn-apply abs">APPLY NOW</div>
</header>

<section class="hero abs" role="img" aria-label="Photo of a young couple meeting a smiling loan advisor holding a small wooden model house"></section>
<h1 class="hero-title abs" style="top:150px">MORTGAGE REFINANCE LOANS</h1>
<p class="hero-lead abs" style="top:204px">Lorem ipsum dolor sit amet, consectetur adipiscing elit, sed do<br>eiusmod tempor incididunt ut labore et dolore</p>
<div class="btn-outline abs" style="top:259px">GET STARTED</div>
<svg class="slider-lines abs" style="top:186px" width="40" height="32" viewBox="0 0 40 32">
  <line x1="3" y1="2" x2="35" y2="2" stroke="#fff" stroke-width="1"/>
  <line x1="0" y1="15" x2="38" y2="15" stroke="#c4001f" stroke-width="2"/>
  <line x1="3" y1="28" x2="35" y2="28" stroke="#fff" stroke-width="1"/>
</svg>

<div class="red-rule abs"></div>
<section class="light-section abs"></section>

<div class="feature-pill abs">
  <div class="feature feature--calc">
    <div class="feature-icon" role="img" aria-label="Icon of a calculator with a money bag"></div>
    <div><h3>MORTGAGE CALCULATOR</h3><p>See how much you can afford by home<br>price, Monthly Payment, or Income</p></div>
  </div>
  <div class="feature feature--home">
    <div class="feature-icon" role="img" aria-label="Icon of a house with coins and a calculator"></div>
    <div><h3>HOME VALUE CHECKER</h3><p>Should you refinance? This calculator<br>breaks down monthly and lifetime cost</p></div>
  </div>
</div>

<p class="kicker abs">2019 Mortgage Loan Limits For</p>
<h2 class="limits-title abs">Conventional, FHA, &amp; VA Loans</h2>
<p class="limits-text abs">Mortgage loan limits for every U.S. county, as published by Crescent Loan Agency &amp; Harbor Home Finance, the<br>Federal Housing Administration (FHA), and the Department of Veterans Affairs (VA)</p>

<div class="search abs">
  <span>your search...</span>
  <div class="search-btn">
    <svg width="16" height="16" viewBox="0 0 16 16" fill="none" stroke="#fff" stroke-width="1.6"><circle cx="6.5" cy="6.5" r="5"/><line x1="10.3" y1="10.3" x2="15" y2="15"/></svg>
  </div>
</div>

<div class="neighborhood abs" role="img" aria-label="Light line drawing of a row of suburban houses, trees and clouds"></div>

<section class="cta abs" role="img" aria-label="Darkened aerial photo of a leafy residential neighbourhood"></section>
<p class="cta-kicker abs">Connect with America’s</p>
<h2 class="cta-title abs">Lending Experts Today!</h2>
<div class="btn-phone abs">
  <svg width="20" height="20" viewBox="0 0 24 24" fill="none" stroke="#fff" stroke-width="1.5" stroke-linejoin="round"><path d="M5 3h4l2 5-2.5 1.5a11 11 0 0 0 6 6L16 13l5 2v4a2 2 0 0 1-2 2A16 16 0 0 1 3 5a2 2 0 0 1 2-2z"/></svg>
  <span>(555) 014-2290</span>
</div>

<footer class="site-footer">
  <div class="brand abs" style="color:var(--red-dark)"><span class="brand-mark"></span>Hearthline</div>
  <div class="socials abs">
    <i style="background:#3b5998"></i><i style="background:#1da1f2"></i><i style="background:#c4001f"></i><i style="background:#f26522"></i>
  </div>
  <p class="copyright abs">2009-2019 Copyright <b>Hearthline, Inc.</b><br>All rights reserved.</p>
  <div class="foot-col abs" style="left:323px;top:1071px">
    <h4>LINKS</h4>
    <ul><li>Get a Mortgage Rate Now</li><li>Loan Types</li><li>Hearthline Disclosures</li><li>Conforming, VA &amp; FHA Loan Limits</li></ul>
  </div>
  <div class="foot-col abs" style="left:543px;top:1077px">
    <h4>COMPANY</h4>
    <ul><li>About Us</li><li>Careers</li><li>Hearthline Resources</li><li>Contact</li></ul>
  </div>
  <div class="foot-col abs" style="left:675px;top:1077px">
    <h4>POLICIES</h4>
    <ul><li>Security Policy</li><li>Privacy Policy</li><li>Terms of Use</li><li>Email Policy</li></ul>
  </div>
</footer>

</body>
</html>
```